Ferris Contracting LLC Business Card Design

I am looking for a creative and unique business card design. We are a commercial construction general contractor. With the name "FERRIS" Contracting, I am hoping to see some neat designs that correlate with the name.

```html
<!DOCTYPE html>
<html lang="en">
<head>
<meta charset="utf-8">
<title>Ferris Contracting LLC – Business Card</title>
<link href="https://fonts.googleapis.com/css2?family=Roboto+Condensed:wght@300;400;700&display=swap" rel="stylesheet">
<style>
  :root {
    --page: #ffffff;
    --steel-light: #f1f1f1;
    --steel-mid: #d2d2d2;
    --steel-dark: #a9a9a9;
    --brand-blue: #1f7fc9;
    --brand-blue-deep: #1b65b0;
    --charcoal: #3b3b3d;
    --ink: #000000;
    --paper: #ffffff;
  }
  * { margin: 0; padding: 0; box-sizing: border-box; }
  html, body {
    width: 1200px; height: 1200px; overflow: hidden;
    background: var(--page);
    font-family: "Roboto Condensed", "Arial Narrow", sans-serif;
  }
  .card {
    position: absolute; left: 263px;
    width: 651px; height: 372px; overflow: hidden;
  }
  .card--front {
    top: 189px;
    background: linear-gradient(180deg, var(--steel-mid) 0%, var(--steel-light) 18%, var(--steel-mid) 45%, #e6e6e6 70%, var(--steel-mid) 100%);
    border: 1px solid #c9c9c9;
  }
  .card__swoosh { position: absolute; inset: 0; width: 100%; height: 100%; }
  .wordmark {
    position: absolute; left: 0; right: 0; top: 160px;
    display: flex; align-items: center; justify-content: center; gap: 14px;
  }
  .wordmark__dot {
    width: 26px; height: 26px; border-radius: 50%;
    background: var(--brand-blue);
  }
  .wordmark__name {
    font-weight: 700; font-size: 46px; letter-spacing: 2px;
    color: var(--brand-blue); line-height: 1;
  }
  .card--back {
    top: 619px; background: var(--charcoal);
  }
  .blade-area {
    position: absolute; left: 24px; top: -126px;
    width: 588px; height: 588px; border-radius: 50%;
    background: radial-gradient(circle, #c4c4c4 60%, #9e9e9e 100%);
  }
  .contact-disc {
    position: absolute; left: 74px; top: -76px;
    width: 488px; height: 488px; border-radius: 50%;
    background: var(--ink);
  }
  .contact {
    position: absolute; left: 0; right: 0; top: 0;
    text-align: center; color: var(--paper);
  }
  .contact__company { position: absolute; left: 0; right: 0; top: 50px; font-weight: 700; font-size: 35px; }
  .contact__person { position: absolute; left: 0; right: 0; top: 94px; font-weight: 700; font-size: 30px; color: var(--brand-blue); }
  .contact__lines { position: absolute; left: 0; right: 0; top: 156px; font-weight: 300; font-size: 28px; line-height: 32.5px; }
  .contact__label { color: var(--brand-blue); }
  .contact__address { position: absolute; left: 0; right: 0; top: 281px; font-weight: 300; font-size: 28px; line-height: 32.5px; }
</style>
</head>
<body>
  <section class="card card--front">
    <svg class="card__swoosh" viewBox="0 0 651 372" aria-hidden="true">
      <path d="M13 30 L36 0 L42 0 L17 28 Z" fill="var(--brand-blue-deep)"/>
      <path d="M29 27 L57 0 L85 0 Q55 18 29 27 Z" fill="var(--steel-dark)"/>
      <path d="M505 372 Q580 340 651 325 L651 332 Q590 350 555 372 Z" fill="var(--steel-dark)"/>
      <path d="M590 372 Q620 358 651 344 L651 358 Q635 365 605 372 Z" fill="var(--brand-blue-deep)"/>
    </svg>
    <div class="wordmark">
      <span class="wordmark__dot"></span>
      <span class="wordmark__name">FERRIS CONTRACTING</span>
    </div>
  </section>

  <section class="card card--back">
    <div class="blade-area" role="img" aria-label="Large circular steel saw blade behind the contact details"></div>
    <div class="contact-disc"></div>
    <div class="contact">
      <p class="contact__company">Ferris Contracting LLC</p>
      <p class="contact__person">Sam Porter, President</p>
      <p class="contact__lines">
        <span class="contact__label">Phone:</span> 555-201-7788<br>
        <span class="contact__label">Email:</span> sam@ferriscontracting.com<br>
        <span class="contact__label">Website:</span> www.ferriscontracting.com
      </p>
      <p class="contact__address">48 Girder Lane,<br>Millbrook, ST 40512</p>
    </div>
  </section>
</body>
</html>
```